Recruitment technology firm needs a downloadable pdf to generate leads.

We need design work for a downloadable pdf that will serve as an educational document to visitors to our website. We help clients identify candidates that fit their job posting. We do that by defining the personality of the job and then assessing the personality of the candidates. We then mathematically compare and rank all the candidates against the job. Our colour scheme is blue. The final design should move from communicating a lack of fit or frustration to people fitting their job and success per the text we have built. People who download this lead generator will be added to our email list for re-marketing purposes. our website is www.brindlewaveadvisory.com. I've attached an example of a lead generator (ebike)for a business unrelated to ours.

Target Market(s)

Our target market is businesses of 50-300 people, we're targeting business owners or executives of entrepreneurial (vs. corporate) companies.

Colors
85acd3
3377b5
0455a3

Requirements
Must have
• Easy to read so text isn't overwhelming.
Nice to have
• Don't be compelled to use our website photos or those like it. I'd like this to reflect entrepreneurial companies, not corporate, suit and tie companies.

```html
<!DOCTYPE html>
<html lang="en">
<head>
<meta charset="utf-8">
<title>5 Reasons You Suck at Hiring for Fit – Brindlewave</title>
<link href="https://fonts.googleapis.com/css2?family=Catamaran:wght@400;500;600;700;800&display=swap" rel="stylesheet">
<style>
:root{
  --teal:#3dd8d8;
  --teal-soft:#6fe2e6;
  --cyan:#00c3ef;
  --cyan-text:#19c6ee;
  --mint:#e8fbfa;
  --ink:#1b1b1b;
  --ink-soft:#333;
  --black:#0b0b0b;
  --white:#ffffff;
  --grid:#9aa4aa;
  --job-red:#f0184f;
  --page-edge:#e3e3e3;
}
*{box-sizing:border-box;margin:0;padding:0}
html,body{width:1200px;height:573px;overflow:hidden;background:var(--white)}
body{position:relative;font-family:"Catamaran",sans-serif;color:var(--ink)}

.page{position:absolute;top:20px;width:377px;height:532px;background:var(--white);outline:1px solid var(--page-edge);overflow:hidden}
.page--cover{left:17px}
.page--reasons{left:415px}
.page--results{left:809px}

.footer-band{position:absolute;left:0;right:0;bottom:0;height:8px;background:var(--teal)}
.footer-band span{position:absolute;right:26px;top:1px;font-size:3.5px;color:var(--white)}

.brand{font-family:"Catamaran",sans-serif;font-weight:600;color:var(--white);letter-spacing:.06em;display:flex;align-items:center;gap:4px}
.brand::before{content:"";width:9px;height:9px;border-radius:50%;background:var(--cyan)}
.brand-tab{position:absolute;top:0;left:212px;width:123px;height:55px;background:var(--black);border-bottom-left-radius:14px;display:flex;align-items:flex-end;justify-content:center;padding-bottom:12px}
.brand-tab .brand{font-size:13px}

/* cover */
.hero{position:absolute;left:0;top:0;width:377px;height:265px;border-bottom-right-radius:62px;overflow:hidden;
  background:linear-gradient(125deg,#4b3f3a 0%,#7d6d64 35%,#a4958a 55%,#6e6058 80%,#54463f 100%)}
.hero-photo{position:absolute;inset:0;background:radial-gradient(ellipse at 55% 60%,rgba(214,196,182,.55),rgba(0,0,0,0) 60%)}
.hero .brand{position:absolute;left:244px;top:26px;font-size:15px}
.hero-title{position:absolute;left:38px;top:41px;color:var(--white);font-weight:800;line-height:.95;text-transform:uppercase}
.hero-title .l1,.hero-title .l2{display:block;font-size:27px;letter-spacing:.01em}
.hero-title .l3{display:block;font-size:41px;margin-top:2px}
.hero-title .l3 small{font-size:25px}
.hero-tag{position:absolute;left:31px;top:188px;color:var(--white);font-weight:700;font-size:23px;line-height:25px}
.hero-sub{position:absolute;left:33px;top:234px;color:var(--white);font-size:16px;font-weight:500}

.intro{position:absolute;left:35px;top:277px;width:305px;font-style:italic;font-size:8.2px;line-height:11.2px;color:var(--ink)}
.goal{position:absolute;left:35px;top:326px;font-size:7.6px;font-weight:700;color:var(--cyan-text)}

.panel{position:absolute;background:var(--mint);border-top-right-radius:28px;padding-top:6px}
.page--cover .panel{left:34px;top:345px;width:299px;height:179px}
.page--reasons .panel{left:35px;top:66px;width:299px;height:270px;border-top-right-radius:26px}

.reason{display:flex;margin-bottom:6px}
.reason-num{flex:0 0 22px;height:17px;background:var(--teal);border-radius:0 9px 9px 0;font-weight:800;font-size:12px;line-height:19px;padding-left:5px;color:var(--ink)}
.reason-body{padding-left:8px;padding-right:10px}
.reason-body h3{font-size:9.6px;line-height:11px;font-weight:700;color:var(--ink);margin-top:4px;margin-bottom:3px}
.reason-body p{font-size:7.9px;line-height:10.7px;color:var(--ink-soft)}
.page--reasons .reason{margin-bottom:5px}
.page--reasons .reason-body h3{margin-top:3px;margin-bottom:2px}

/* reasons page */
.banner{position:absolute;left:35px;width:300px;background:var(--teal);border-radius:4px;color:var(--white);font-weight:700;text-align:center}
.page--reasons .banner{top:346px;height:18px;font-size:12px;line-height:20px}
.how-list{position:absolute;left:41px;top:372px;width:290px;list-style:none;font-size:7.4px;line-height:7.9px;color:var(--ink)}
.how-list li{position:relative;padding-left:7px;margin-bottom:4.3px}
.how-list li::before{content:"";position:absolute;left:0;top:2.4px;width:2.6px;height:2.6px;background:var(--ink-soft)}
.how-list li.note{padding-left:7px}
.how-list li.note::before{display:none}

/* results page */
.fit-chart{position:absolute;left:35px;top:71px}
.fit-chart text{font-family:"Catamaran",sans-serif}
.next-title{position:absolute;left:35px;top:222px;color:var(--cyan-text);font-weight:800;line-height:.8}
.next-title .small{display:block;font-size:15px}
.next-title .big{display:block;font-size:31px}
.steps{position:absolute;left:35px;top:264px;width:299px;display:flex;gap:8px}
.step{flex:1;height:56px;background:var(--cyan);border-radius:5px;color:var(--white);font-size:7px;line-height:8px;text-align:center;display:flex;align-items:center;justify-content:center;padding:0 10px}
.page--results .banner{top:331px;height:21px;font-size:13px;line-height:23px}
.quotes{position:absolute;left:37px;top:361px;width:295px}
.quote{position:relative;padding-left:11px;margin-bottom:4px;font-size:5.6px;line-height:7.5px;color:var(--ink-soft)}
.quote::before{content:"\201C";position:absolute;left:0;top:-1px;font-size:13px;line-height:13px;font-weight:700;color:var(--teal)}
.quote cite{display:block;font-style:normal;margin-top:4px;color:var(--ink)}
.contact{position:absolute;left:0;right:0;top:494px;display:flex;justify-content:center;align-items:center;gap:6px;font-size:8.5px;color:var(--ink)}
.contact-item{display:flex;align-items:center;gap:4px}
.contact-divider{width:1px;height:12px;background:var(--cyan)}
</style>
</head>
<body>

<!-- Page 1: Cover -->
<section class="page page--cover">
  <div class="hero">
    <div class="hero-photo" role="img" aria-label="Photo of two people across a table in a tense hiring conversation"></div>
    <div class="brand">BRINDLEWAVE</div>
    <h1 class="hero-title">
      <span class="l1">5 Reasons</span>
      <span class="l2">You Suck At</span>
      <span class="l3">Hiring <small>for fit.</small></span>
    </h1>
    <p class="hero-tag">Hiring the wrong fit is painful,<br>we are with you there.</p>
    <p class="hero-sub">Bad hires ruin your day, every day.</p>
  </div>

  <p class="intro">You want to make sure your next hire is the right one. You know what it's like when you hire the wrong person – they aren't productive, they don't get along with others, there's tension, you have to let them go, and you re-start the whole process over again.</p>
  <p class="goal">Our goal is to help you stop this cycle. Here are 5 mistakes you are likely making.</p>

  <div class="panel">
    <div class="reason">
      <div class="reason-num">1.</div>
      <div class="reason-body">
        <h3>You have not defined the obstacles found in the job.</h3>
        <p>Every job has its challenges and you need to find someone who will deal with the challenges as a high performer would. Spending too much time in unstructured conversation or putting too much emphasis on selling the role can detract from this key insight. Define the top 2-5 obstacles and learn how the candidate has or would tackle them.</p>
      </div>
    </div>
    <div class="reason">
      <div class="reason-num">2.</div>
      <div class="reason-body">
        <h3>You describe the job using words, not data.</h3>
        <p>Detail oriented means different things to different people. You only find out after you have hired someone that they are not detailed enough (or are too detailed!). The same can happen when we say a candidate needs to be proactive or risk oriented. You only find out later that you hired too much or too little. You used words and not numbers to define what you needed for the role.</p>
      </div>
    </div>
  </div>
  <div class="footer-band"><span>Pg.1</span></div>
</section>

<!-- Page 2: Reasons 3–5 -->
<section class="page page--reasons">
  <div class="brand-tab"><div class="brand">BRINDLEWAVE</div></div>

  <div class="panel">
    <div class="reason">
      <div class="reason-num">3.</div>
      <div class="reason-body">
        <h3>You assume knowledge and experience<br>equals performance.</h3>
        <p>Just because someone's resume says they are a strong manager does not mean they are one. And yet this is how you screen and rank your candidates. The best resumes rise to the top. But resumes are a terrible predictor of performance. Success at one company does not mean success in yours. Who are you overlooking that may be a better performer? (we have an idea below)</p>
      </div>
    </div>
    <div class="reason">
      <div class="reason-num">4.</div>
      <div class="reason-body">
        <h3>You are biased and subjective in your<br>assessment of others.</h3>
        <p>You get attracted to certain resumes and backgrounds. You make judgement calls on phone interviews. You do the same when you meet someone and during an interview. Very few recruitment processes have a way of OBJECTIVELY ranking and comparing candidates. As a result we end up picking someone we like as opposed to someone who will excel in the job.</p>
      </div>
    </div>
    <div class="reason">
      <div class="reason-num">5.</div>
      <div class="reason-body">
        <h3>You think your “gut” makes good decisions</h3>
        <p>“Gut” has more to do with how likeable someone is than how effective they will be. Effectiveness comes from a person's ability to consistently behave in a manner that produces exceptional results. Do not make judgement calls on behaviours a candidate shows but may not be able to consistently repeat.</p>
      </div>
    </div>
  </div>

  <div class="banner">So how can you hire for fit?</div>
  <ul class="how-list">
    <li>Personality is the most significant predictor of both fit to the manager and performance in the role. It is also one of the most difficult things to assess without the use of an objective tool.</li>
    <li>Most candidates behave a certain way in an interview, but it may be something that is difficult for them to sustain.</li>
    <li>To start addressing the problem of hiring bad fits you need to add more objectivity to your process. FitGauge is a tool designed to define a benchmark of what personality is required in a role using data. Everyone gets on the same page of what success looks like.</li>
    <li>From there each candidate completes a Profile personality survey within the <strong>FitGauge tool.</strong> Then they are compared equally to the benchmark and ranked objectively. All candidates are compared using the same personality dimensions.</li>
    <li>You leverage specific data and our insight to find the best candidates …Your ability to consistently hire above average fits increases … You achieve more.</li>
    <li class="note">Here are the results of a candidate compared to a job. The job is represented in red, the candidate is represented in black.</li>
  </ul>
  <div class="footer-band"><span>Pg.2</span></div>
</section>

<!-- Page 3: Results & next steps -->
<section class="page page--results">
  <div class="brand-tab"><div class="brand">BRINDLEWAVE</div></div>

  <svg class="fit-chart" width="300" height="136" viewBox="0 0 643 291" role="img" aria-label="Personality profile chart comparing a job benchmark in red with a candidate in black">
    <rect x="0" y="0" width="643" height="291" fill="#fff" stroke="#8c959b" stroke-width="1.5"/>
    <!-- label columns -->
    <rect x="0" y="0" width="100" height="143" fill="#36c9d1"/>
    <rect x="0" y="163" width="100" height="105" fill="#6ed6dd"/>
    <rect x="0" y="143" width="643" height="20" fill="#e4e7e9"/>
    <rect x="0" y="268" width="643" height="23" fill="#e4e7e9"/>
    <g stroke="#8c959b" stroke-width="1.2">
      <line x1="0" y1="35" x2="643" y2="35"/><line x1="0" y1="71" x2="643" y2="71"/>
      <line x1="0" y1="107" x2="643" y2="107"/><line x1="0" y1="143" x2="643" y2="143"/>
      <line x1="0" y1="163" x2="643" y2="163"/><line x1="0" y1="198" x2="643" y2="198"/>
      <line x1="0" y1="233" x2="643" y2="233"/><line x1="0" y1="268" x2="643" y2="268"/>
    </g>
    <line x1="371" y1="2" x2="371" y2="143" stroke="#b9bfc3" stroke-width="1.2" stroke-dasharray="4 4"/>
    <g fill="#fff" font-size="8.5" font-weight="700">
      <text x="8" y="21">ASSERTIVENESS</text>
      <text x="8" y="57">SOCIABILITY</text>
      <text x="8" y="92">PACE</text>
      <text x="8" y="122">DETAIL</text><text x="8" y="132">ORIENTATION</text>
      <text x="8" y="178">BEHAVIORAL</text><text x="8" y="188">ADAPTABILITY</text>
      <text x="8" y="219">EMOTIVENESS</text>
      <text x="8" y="254">CREATIVITY</text>
    </g>
    <g fill="#333" font-size="10" text-anchor="middle">
      <text x="123" y="157">-5</text><text x="172" y="157">-4</text><text x="222" y="157">-3</text>
      <text x="271" y="157">-2</text><text x="320" y="157">-1</text><text x="371" y="157">0</text>
      <text x="419" y="157">1</text><text x="468" y="157">2</text><text x="518" y="157">3</text>
      <text x="567" y="157">4</text><text x="616" y="157">5</text>
      <text x="125" y="284">0</text><text x="174" y="284">1</text><text x="223" y="284">2</text>
      <text x="272" y="284">3</text><text x="321" y="284">4</text><text x="371" y="284">5</text>
      <text x="420" y="284">6</text><text x="469" y="284">7</text><text x="518" y="284">8</text>
      <text x="567" y="284">9</text><text x="616" y="284">10</text>
    </g>
    <polyline points="448,13 418,52 273,87 353,122" fill="none" stroke="var(--job-red)" stroke-width="2" stroke-dasharray="3 3"/>
    <polyline points="463,14 348,48 323,87 368,122" fill="none" stroke="#111" stroke-width="2"/>
    <g fill="var(--job-red)">
      <rect x="443" y="8" width="10" height="10"/><rect x="413" y="47" width="10" height="10"/>
      <rect x="268" y="82" width="10" height="10"/><rect x="348" y="117" width="10" height="10"/>
      <rect x="416" y="176" width="10" height="10"/><rect x="416" y="212" width="10" height="10"/>
      <rect x="416" y="247" width="10" height="10"/>
    </g>
    <g fill="#111">
      <circle cx="463" cy="14" r="5"/><circle cx="348" cy="48" r="5"/>
      <circle cx="323" cy="87" r="5"/><circle cx="368" cy="122" r="5"/>
      <circle cx="503" cy="181" r="5"/><circle cx="571" cy="217" r="5"/>
      <circle cx="438" cy="252" r="5"/>
    </g>
  </svg>

  <h2 class="next-title"><span class="small">What's</span><span class="big">next?</span></h2>
  <div class="steps">
    <div class="step">Contact us to discuss your position</div>
    <div class="step">Leverage our tools, process and insights throughout your process</div>
    <div class="step">Welcome a great new team member and crush your goals</div>
  </div>

  <div class="banner">What FitGauge users are saying… ”</div>
  <div class="quotes">
    <blockquote class="quote">The process changes we have made in recruiting as a result of working with Brindlewave's FitGauge have been transformational. We went into the interviews with confidence which ultimately made it easier to select the right candidate for the roles. Thanks to your tools and assessments I have a stronger team!<cite>- VP, Oil &amp; Gas Sector</cite></blockquote>
    <blockquote class="quote">We've had very good success over the past year and a half since I've been in this role with reducing our turnover from around 50% to less than 10%. I feel very strongly that much of that has to do with our practice of only hiring people who are a match for our benchmarks.<cite>- Recruiter, IT Sector</cite></blockquote>
    <blockquote class="quote">FitGauge allows us to identify those that don't fit our benchmark early so we don't spend time with those that don't fit.<cite>- Owner, Auto Industry</cite></blockquote>
  </div>

  <div class="contact">
    <div class="contact-item">
      <svg width="11" height="8" viewBox="0 0 11 8" aria-hidden="true"><rect x=".5" y=".5" width="10" height="7" rx="1" fill="none" stroke="#1b1b1b"/><polyline points=".8,.8 5.5,4.6 10.2,.8" fill="none" stroke="#1b1b1b"/></svg>
      <span>hello@brindlewaveadvisory.com</span>
    </div>
    <div class="contact-divider"></div>
    <div class="contact-item">
      <svg width="10" height="10" viewBox="0 0 10 10" aria-hidden="true"><circle cx="5" cy="5" r="5" fill="#1b1b1b"/><path d="M3.3 2.4l1 1.1-.5.7c.4.8 1 1.4 1.8 1.8l.7-.5 1.1 1-.6.9c-2-.4-3.9-2.3-4.3-4.3z" fill="#fff"/></svg>
      <span>855 555 0142</span>
    </div>
  </div>
  <div class="footer-band"><span>Pg.3</span></div>
</section>

</body>
</html>
```